Internal Web Pages for Metricsy Hub

I need internal web pages (Why Metricsy Hub?, What We Offer, Blog, Testimonials) that match the design of the homepage. These do not need to be as long or in-depth as the landing page (provided for reference) but I will need three, maybe four, total pages (I'll select the max number of pages for now, but these will all be simple and short pages). Also attached is our new logo design for the company.

They are to essentially be:
Why Metricsy Hub? - An About Us and Why Choose Us page rolled into one.
What We Offer - A Services type page
Blog - self-explanatory
Testimonials - Customer Reviews and Use Cases

Also, maybe a very simple "Contact Us" page as well.

Target Market(s)

Business professionals that work with data analytics teams

Industry/Entity Type

Data Science

Number of Pages Required

5+ page

Requirements
Must have
• It must match the original design in theme and colors.
Nice to have
• Simple pages that show continuity that flows from the original landing page.
Should not have
• Can not be a different design that does not match the landing page.

```html
<!DOCTYPE html>
<html lang="en">
<head>
<meta charset="utf-8">
<title>About Us – Metricsy Hub</title>
<link href="https://fonts.googleapis.com/css2?family=Poppins:wght@400;500;600;700&family=Open+Sans:wght@400;600;700&display=swap" rel="stylesheet">
<style>
:root{
  --purple-deep:#1a0a4c;
  --purple:#2a1470;
  --purple-mid:#3a1f8f;
  --blue:#3d56d6;
  --blue-soft:#6f83ea;
  --orange:#f4801f;
  --ink:#222433;
  --text:#5b5d6b;
  --muted:#9a9cab;
  --white:#ffffff;
  --line:#e6e7ef;
}
*{box-sizing:border-box;margin:0;padding:0}
html,body{width:1200px;height:3588px;overflow:hidden}
body{position:relative;background:var(--white);font-family:"Open Sans",sans-serif;color:var(--text)}
.abs{position:absolute}

/* header */
.site-header{position:absolute;top:0;left:0;width:1200px;height:80px;background:var(--white);z-index:5;display:flex;align-items:center;padding:0 40px 0 40px}
.brand{display:flex;align-items:center;gap:12px;font-family:"Poppins",sans-serif;font-weight:500;font-size:40px;color:var(--purple-mid)}
.brand-mark{width:34px;height:34px;background:var(--blue)}
.nav{display:flex;gap:34px;margin-left:auto;margin-right:40px;font-family:"Poppins",sans-serif;font-size:17px;color:var(--ink)}
.nav .active{color:var(--blue)}
.btn-orange{background:var(--orange);color:var(--white);font-family:"Poppins",sans-serif;font-weight:600;font-size:14px;letter-spacing:1px;padding:14px 24px;border-radius:3px}

/* hero */
.hero{position:absolute;top:80px;left:0;width:1200px;height:560px;clip-path:polygon(0 0,100% 0,100% 86%,50% 100%,0 86%);background:linear-gradient(110deg,#1d2c4a 0%,#2f4f7a 35%,#4a6e95 60%,#22324f 100%)}
.hero-edge{position:absolute;top:545px;left:0;z-index:2}
.hero-title{position:absolute;top:232px;left:84px;color:var(--white);font-family:"Poppins",sans-serif;font-weight:500;font-size:50px;z-index:3}
.hero-sub{position:absolute;top:300px;left:84px;width:330px;color:#dfe4f2;font-size:15px;line-height:1.4;z-index:3}

/* about */
.section-title{font-family:"Poppins",sans-serif;font-weight:400;color:var(--ink);font-size:44px}
.about-title{position:absolute;top:690px;left:140px}
.about-rule{position:absolute;top:754px;left:140px;width:150px;height:2px;background:var(--blue-soft)}
.about-copy{position:absolute;top:800px;left:140px;width:920px;font-size:15px;line-height:1.72;color:var(--text)}

/* collage */
.collage{position:absolute;z-index:3}
.shot-a{left:245px;top:1275px;width:230px;height:290px;background:linear-gradient(160deg,#c9d8e8,#6f8cb3 60%,#3b4f73)}
.shot-b{left:475px;top:1200px;width:225px;height:365px;background:linear-gradient(160deg,#e0e8f3,#8aa9cf 50%,#4a5f86)}
.shot-c{left:700px;top:1125px;width:200px;height:440px;background:linear-gradient(165deg,#5c6b55,#3b4632 50%,#1f2a26)}
.play{position:absolute;left:528px;top:1360px;width:72px;height:72px;border-radius:50%;background:var(--white);z-index:4;display:flex;align-items:center;justify-content:center}

/* why */
.why{position:absolute;top:1500px;left:0;width:1200px;height:900px;background:linear-gradient(180deg,#2b1575 0%,#200d5c 45%,#1b0a50 100%);clip-path:polygon(0 70px,100% 0,100% 100%,0 100%)}
.why-edge{position:absolute;top:1494px;left:0;z-index:2}
.why-title{position:absolute;top:1710px;left:0;width:1200px;text-align:center;color:var(--white)}
.why-rule{position:absolute;top:1772px;left:560px;width:80px;height:2px;background:var(--blue-soft)}
.feature{position:absolute;width:300px;text-align:center;color:var(--white)}
.feature .icon{width:58px;height:58px;border-radius:50%;background:rgba(255,255,255,.1);margin:0 auto 20px;display:flex;align-items:center;justify-content:center}
.feature h3{font-family:"Poppins",sans-serif;font-weight:600;font-size:16px;margin-bottom:8px}
.feature p{font-size:13px;line-height:1.45;color:#b9b3d6}
.why-divider{position:absolute;top:2040px;height:1px;width:380px;background:rgba(255,255,255,.15)}

/* blog */
.blog-title{position:absolute;top:2420px;left:0;width:1200px;text-align:center}
.blog-rule{position:absolute;top:2482px;left:560px;width:80px;height:2px;background:var(--blue-soft)}
.card{position:absolute;top:2532px;width:292px;height:336px;background:var(--white);box-shadow:0 4px 18px rgba(30,20,80,.16)}
.card .media{height:160px;position:relative}
.card .badge{position:absolute;top:0;right:14px;width:44px;height:52px;background:var(--orange);color:var(--white);font-family:"Poppins",sans-serif;font-size:10px;font-weight:600;text-align:center;line-height:1.2;padding-top:10px}
.card h4{font-family:"Poppins",sans-serif;font-weight:600;font-size:13px;color:var(--ink);line-height:1.35;padding:16px 26px 0}
.meta{display:flex;gap:24px;padding:8px 26px 0;font-size:11px;color:var(--text);align-items:center}
.meta span{display:flex;align-items:center;gap:5px}
.card p{font-size:11px;line-height:1.5;padding:10px 26px 0;color:var(--text)}
.learn{position:absolute;left:26px;bottom:20px;border:1.5px solid var(--blue);border-radius:20px;padding:6px 16px;font-family:"Poppins",sans-serif;font-size:10px;font-weight:600;color:var(--blue);display:flex;gap:8px;align-items:center}

/* footer */
.site-footer{position:absolute;top:2940px;left:0;width:1200px;height:540px;background:var(--purple-deep)}
.footer-brand{position:absolute;top:3000px;left:145px;font-size:36px;color:var(--white)}
.footer-brand .brand-mark{width:30px;height:30px;background:var(--blue-soft)}
.footer-about{position:absolute;top:3075px;left:145px;width:270px;font-size:15px;line-height:1.45;color:#c9c3e6}
.socials{position:absolute;top:3190px;left:145px;display:flex;gap:10px}
.socials i{width:34px;height:34px;border-radius:50%;border:1.5px solid #c9c3e6;display:block}
.footer-heading{position:absolute;top:2998px;font-family:"Poppins",sans-serif;font-weight:600;font-size:18px;color:var(--white);letter-spacing:.5px}
.contact-item{position:absolute;left:480px;display:flex;gap:14px;color:var(--white);font-size:15px;line-height:1.4}
.contact-item svg{flex:none;margin-top:3px}
.signup-copy{position:absolute;top:3040px;left:755px;width:300px;font-size:13px;line-height:1.5;color:#c9c3e6}
.email-field{position:absolute;top:3100px;left:755px;width:300px;height:42px;background:var(--white);border-radius:2px;font-size:13px;color:var(--muted);padding:12px 14px}
.subscribe{position:absolute;top:3160px;left:755px;padding:12px 20px;font-size:13px}
.copyright{position:absolute;top:3480px;left:0;width:1200px;height:108px;background:#140740;color:var(--white);font-size:15px;display:flex;align-items:center;justify-content:center}
</style>
</head>
<body>

<header class="site-header">
  <div class="brand"><span class="brand-mark"></span>Metricsy Hub</div>
  <nav class="nav"><span>Home</span><span class="active">About us</span><span>Our Service</span><span>Blog</span><span>Contact</span></nav>
  <span class="btn-orange">GET STARTED</span>
</header>

<section class="hero" role="img" aria-label="Photo of a team member working at a laptop in a dim office with data visuals floating on screens"></section>
<svg class="hero-edge" width="1200" height="100" viewBox="0 0 1200 100"><polyline points="0,18 600,95 1200,18" fill="none" stroke="#3d56d6" stroke-width="6"/></svg>
<h1 class="hero-title">About us</h1>
<p class="hero-sub">Sed ut perspiciatis unde omnis iste natus error sit voluptatem accusantium doloremque.</p>

<h2 class="section-title about-title">About Metricsy Hub</h2>
<div class="about-rule"></div>
<p class="about-copy">Sed ut perspiciatis unde omnis iste natus error sit voluptatem accusantium doloremque laudantium, totam rem aperiam, eaque ipsa quae ab illo inventore veritatis et quasi architecto beatae vitae dicta sunt explicabo. Nemo enim ipsam voluptatem quia voluptas sit aspernatur aut odit aut fugit, sed quia consequuntur magni dolores eos qui ratione voluptatem sequi nesciunt. Neque porro quisquam est, qui dolorem ipsum quia dolor sit amet Sed ut perspiciatis unde omnis iste natus error sit voluptatem accusantium doloremque laudantium, totam rem aperiam, eaque ipsa quae ab illo inventore veritatis et quasi architecto beatae vitae dicta sunt explicabo. Nemo enim ipsam voluptatem quia voluptas sit aspernatur aut odit aut fugit, sed quia consequuntur magni dolores eos qui ratione voluptatem sequi nesciunt. Neque porro quisquam est, qui dolorem ipsum quia dolor sit amet</p>

<section class="why"></section>
<svg class="why-edge" width="1200" height="80" viewBox="0 0 1200 80"><line x1="0" y1="76" x2="1200" y2="6" stroke="#3d56d6" stroke-width="6"/></svg>

<div class="collage shot-a" role="img" aria-label="Photo of a laptop showing analytics charts"></div>
<div class="collage shot-b" role="img" aria-label="Photo of a dashboard on a laptop screen"></div>
<div class="collage shot-c" role="img" aria-label="Photo of a desk with plants and a monitor"></div>
<div class="play"><svg width="26" height="28" viewBox="0 0 26 28"><polygon points="4,2 24,14 4,26" fill="#3d56d6"/></svg></div>

<h2 class="section-title why-title">Why Choose Us</h2>
<div class="why-rule"></div>

<div class="feature" style="left:230px;top:1830px">
  <div class="icon"><svg width="26" height="26" viewBox="0 0 26 26" fill="none" stroke="#fff" stroke-width="1.6"><rect x="4" y="4" width="18" height="18" rx="2"/><path d="M8 17v-4M13 17v-8M18 17v-6"/></svg></div>
  <h3>Neque porro quisquam.</h3>
  <p>Sed ut perspiciatis unde omnis iste natus voluptatem accusantium doloremque</p>
</div>
<div class="feature" style="left:670px;top:1830px">
  <div class="icon"><svg width="26" height="26" viewBox="0 0 26 26" fill="none" stroke="#fff" stroke-width="1.6"><rect x="4" y="4" width="18" height="18" rx="2"/><path d="M8 17v-4M13 17v-8M18 17v-6"/></svg></div>
  <h3>Neque porro quisquam.</h3>
  <p>Sed ut perspiciatis unde omnis iste natus voluptatem accusantium doloremque</p>
</div>
<div class="why-divider" style="left:210px"></div>
<div class="why-divider" style="left:650px"></div>
<div class="feature" style="left:230px;top:2090px">
  <div class="icon"><svg width="26" height="26" viewBox="0 0 26 26" fill="none" stroke="#fff" stroke-width="1.6"><rect x="4" y="4" width="18" height="18" rx="2"/><path d="M8 17v-4M13 17v-8M18 17v-6"/></svg></div>
  <h3>Neque porro quisquam.</h3>
  <p>Sed ut perspiciatis unde omnis iste natus voluptatem accusantium doloremque</p>
</div>
<div class="feature" style="left:670px;top:2090px">
  <div class="icon"><svg width="26" height="26" viewBox="0 0 26 26" fill="none" stroke="#fff" stroke-width="1.6"><rect x="4" y="4" width="18" height="18" rx="2"/><path d="M8 17v-4M13 17v-8M18 17v-6"/></svg></div>
  <h3>Neque porro quisquam.</h3>
  <p>Sed ut perspiciatis unde omnis iste natus voluptatem accusantium doloremque</p>
</div>

<h2 class="section-title blog-title">From The Blog</h2>
<div class="blog-rule"></div>

<article class="card" style="left:140px">
  <div class="media" role="img" aria-label="Photo of a presenter pointing at a screen of charts" style="background:linear-gradient(150deg,#e9eef6,#9fb6d6 55%,#5a6f98)"><span class="badge">12<br>JUL</span></div>
  <h4>NEMO ENIM IPSAM VOLUPTA QUIA VOLUPTAS SIT</h4>
  <div class="meta"><span><svg width="12" height="12" viewBox="0 0 12 12" fill="none" stroke="#3d56d6" stroke-width="1.3"><path d="M1 2h10v6H5l-3 3V8H1z"/></svg>2 comments</span><span><svg width="12" height="12" viewBox="0 0 12 12" fill="#3d56d6"><circle cx="6" cy="4" r="2.5"/><path d="M1 11c0-3 2.5-4.5 5-4.5s5 1.5 5 4.5z"/></svg>by Daniel</span></div>
  <p>Sed ut perspiciatis unde omnis iste natus error sit voluptatem accusantium dolore lauda</p>
  <span class="learn">LEARN MORE <svg width="10" height="10" viewBox="0 0 10 10" fill="none" stroke="#3d56d6" stroke-width="1.5"><path d="M1 5h8M6 2l3 3-3 3"/></svg></span>
</article>
<article class="card" style="left:454px">
  <div class="media" role="img" aria-label="Photo of an analyst holding a tablet in front of glowing data" style="background:linear-gradient(150deg,#3a2a2a,#7a5a48 50%,#1d2230)"><span class="badge">12<br>JUL</span></div>
  <h4>NEMO ENIM IPSAM VOLUPTA QUIA VOLUPTAS SIT</h4>
  <div class="meta"><span><svg width="12" height="12" viewBox="0 0 12 12" fill="none" stroke="#3d56d6" stroke-width="1.3"><path d="M1 2h10v6H5l-3 3V8H1z"/></svg>2 comments</span><span><svg width="12" height="12" viewBox="0 0 12 12" fill="#3d56d6"><circle cx="6" cy="4" r="2.5"/><path d="M1 11c0-3 2.5-4.5 5-4.5s5 1.5 5 4.5z"/></svg>by Daniel</span></div>
  <p>Sed ut perspiciatis unde omnis iste natus error sit voluptatem accusantium dolore lauda</p>
  <span class="learn">LEARN MORE <svg width="10" height="10" viewBox="0 0 10 10" fill="none" stroke="#3d56d6" stroke-width="1.5"><path d="M1 5h8M6 2l3 3-3 3"/></svg></span>
</article>
<article class="card" style="left:768px">
  <div class="media" role="img" aria-label="Illustration of a glowing digital data network in blue tones" style="background:linear-gradient(150deg,#0f2348,#2e5aa0 55%,#0c1630)"><span class="badge">12<br>JUL</span></div>
  <h4>NEMO ENIM IPSAM VOLUPTA QUIA VOLUPTAS SIT</h4>
  <div class="meta"><span><svg width="12" height="12" viewBox="0 0 12 12" fill="none" stroke="#3d56d6" stroke-width="1.3"><path d="M1 2h10v6H5l-3 3V8H1z"/></svg>2 comments</span><span><svg width="12" height="12" viewBox="0 0 12 12" fill="#3d56d6"><circle cx="6" cy="4" r="2.5"/><path d="M1 11c0-3 2.5-4.5 5-4.5s5 1.5 5 4.5z"/></svg>by Daniel</span></div>
  <p>Sed ut perspiciatis unde omnis iste natus error sit voluptatem accusantium dolore lauda</p>
  <span class="learn">LEARN MORE <svg width="10" height="10" viewBox="0 0 10 10" fill="none" stroke="#3d56d6" stroke-width="1.5"><path d="M1 5h8M6 2l3 3-3 3"/></svg></span>
</article>

<footer class="site-footer"></footer>
<div class="brand footer-brand abs"><span class="brand-mark"></span>Metricsy Hub</div>
<p class="footer-about">Sed ut perspiciatis unde omnis iste natus error sit voluptatem accusantium doloremque, totam rem aperiam, eaque ipsa quae ab illo inventore veritatis et quasi.</p>
<div class="socials"><i></i><i></i><i></i><i></i></div>

<h5 class="footer-heading" style="left:480px">CONTACT US</h5>
<div class="contact-item" style="top:3045px"><svg width="16" height="18" viewBox="0 0 16 18" fill="none" stroke="#fff" stroke-width="1.5"><path d="M8 17s6-6 6-10A6 6 0 0 0 2 7c0 4 6 10 6 10z"/><circle cx="8" cy="7" r="2"/></svg><span>Metricsy Hub<br>250 ipsum voluptatem<br>quia voluptas</span></div>
<div class="contact-item" style="top:3135px"><svg width="16" height="16" viewBox="0 0 16 16" fill="none" stroke="#fff" stroke-width="1.5"><path d="M3 1h3l1.5 4-2 1.5a9 9 0 0 0 4 4l1.5-2 4 1.5v3a2 2 0 0 1-2 2A14 14 0 0 1 1 3a2 2 0 0 1 2-2z"/></svg><span>Phone:<br>555-0142-2200</span></div>
<div class="contact-item" style="top:3200px"><svg width="16" height="14" viewBox="0 0 16 14" fill="none" stroke="#fff" stroke-width="1.5"><rect x="1" y="1" width="14" height="12"/><path d="M1 1l7 6 7-6"/></svg><span>Email :<br>info@metricsyhub.com</span></div>

<h5 class="footer-heading" style="left:755px">SIGN UP TO RECEIVE EMAIL</h5>
<p class="signup-copy">Excepteur sint occaecat cupidatat non proident, sunt in culpa qui officia sed quia non.</p>
<div class="email-field">Enter Email</div>
<span class="btn-orange subscribe abs">SUBSCRIBE</span>

<div class="copyright">Copyright © Metricsy Hub 2021. All rights reserved. | Privacy Policy</div>

</body>
</html>
```